Business Card Design Project Lend Aid

Simple and clean business card,

Logo and fond added in attachment

Data need to be changable:
Ria Vondeck
Customer Service Specialist

Lend Aid - ria.vondeck@lendaid.be - Mob: +32491532876 - www.lendaid.be

Target Market(s)

Small businesses

Industry/Entity Type

Business

Requirements
Nice to have
• QR-code

```html
<!DOCTYPE html>
<html lang="en">
<head>
<meta charset="utf-8">
<title>Lend Aid – Business Card</title>
<link href="https://fonts.googleapis.com/css2?family=Mulish:wght@400;700&family=Questrial&display=swap" rel="stylesheet">
<style>
  :root {
    --backdrop: #2c2c2e;
    --paper: #f5f5f3;
    --brand-blue: #4f9ad8;
    --ink-blue: #2a78c0;
    --soft-blue: #6fb0e4;
    --circuit-green: #8dc63f;
    --navy-light: #5a86b2;
    --navy-dark: #2d5a8a;
    --white: #ffffff;
  }
  * { margin: 0; padding: 0; box-sizing: border-box; }
  html, body { width: 1200px; height: 800px; overflow: hidden; }
  body {
    background: var(--backdrop);
    font-family: "Mulish", sans-serif;
  }
  .stage {
    position: relative;
    width: 1200px;
    height: 800px;
  }
  .card {
    position: absolute;
    top: 257px;
    width: 500px;
    height: 286px;
    border-radius: 3px;
    overflow: hidden;
    box-shadow: 0 8px 24px rgba(0,0,0,0.45);
  }
  .card--front { left: 70px; background: var(--paper); }
  .card--back {
    left: 630px;
    background: linear-gradient(135deg, var(--navy-light) 0%, var(--navy-dark) 100%);
  }
  .circuit {
    position: absolute;
    inset: 0;
    width: 100%;
    height: 100%;
  }
  .brand {
    position: absolute;
    display: flex;
    align-items: center;
    gap: 14px;
  }
  .brand__mark {
    width: 44px;
    height: 44px;
    border: 6px solid var(--brand-blue);
    border-radius: 8px;
  }
  .brand__name {
    font-family: "Questrial", sans-serif;
    font-size: 46px;
    line-height: 1;
    letter-spacing: -0.5px;
  }
  .card--front .brand { left: 150px; top: 66px; }
  .card--front .brand__name { color: var(--brand-blue); }
  .card--back .brand { left: 120px; top: 104px; }
  .card--back .brand__mark { width: 60px; height: 60px; border-color: var(--soft-blue); border-width: 8px; border-radius: 10px; }
  .card--back .brand__name { color: var(--white); font-size: 60px; }

  .contact {
    position: absolute;
    right: 28px;
    bottom: 26px;
    text-align: right;
    color: var(--ink-blue);
  }
  .contact__name { font-weight: 700; font-size: 17px; }
  .contact__role {
    font-family: "Questrial", sans-serif;
    font-size: 15px;
    color: var(--soft-blue);
    margin-bottom: 10px;
  }
  .contact__line {
    display: flex;
    justify-content: flex-end;
    align-items: center;
    gap: 8px;
    font-weight: 700;
    font-size: 15px;
    line-height: 24px;
  }
  .contact__line--plain { font-weight: 400; }
  .contact__icon { width: 14px; height: 14px; flex: none; }
</style>
</head>
<body>
<main class="stage">

  <section class="card card--front" aria-label="Business card front">
    <svg class="circuit" viewBox="0 0 500 286" role="img" aria-label="Green circuit-board pattern across the top-left corner">
      <polygon points="0,0 150,0 0,150" fill="var(--circuit-green)"/>
    </svg>

    <div class="brand">
      <span class="brand__mark" aria-hidden="true"></span>
      <span class="brand__name">Lend Aid</span>
    </div>

    <div class="contact">
      <p class="contact__name">Ria Vondeck</p>
      <p class="contact__role">Customer Service Specialist</p>
      <p class="contact__line">+32491532876
        <svg class="contact__icon" viewBox="0 0 14 14" aria-hidden="true"><path d="M3 1h3l1 3-2 1.5a8 8 0 0 0 3.5 3.5L10 7l3 1v3a2 2 0 0 1-2 2A11 11 0 0 1 1 3a2 2 0 0 1 2-2z" fill="var(--circuit-green)"/></svg>
      </p>
      <p class="contact__line contact__line--plain">ria.vondeck@lendaid.be
        <svg class="contact__icon" viewBox="0 0 14 14" aria-hidden="true"><rect x="1" y="3" width="12" height="8" fill="var(--circuit-green)"/><path d="M1 3l6 5 6-5" stroke="var(--paper)" stroke-width="1.2" fill="none"/></svg>
      </p>
      <p class="contact__line">www.lendaid.be
        <svg class="contact__icon" viewBox="0 0 14 14" aria-hidden="true"><circle cx="7" cy="7" r="6" fill="var(--circuit-green)"/><path d="M1 7h12M7 1v12M7 1c-3 3-3 9 0 12M7 1c3 3 3 9 0 12" stroke="var(--paper)" stroke-width="1" fill="none"/></svg>
      </p>
    </div>
  </section>

  <section class="card card--back" aria-label="Business card back">
    <svg class="circuit" viewBox="0 0 500 286" role="img" aria-label="Green circuit-board pattern along the bottom-right corner">
      <polygon points="500,120 500,286 260,286" fill="var(--circuit-green)"/>
    </svg>

    <div class="brand">
      <span class="brand__mark" aria-hidden="true"></span>
      <span class="brand__name">Lend Aid</span>
    </div>
  </section>

</main>
</body>
</html>
```